Post card for landscape service

Velmora Property Management**FEATURED SERVICE*** Weekly Lawn mowing service starting at $15/ cutting ****other services****landscape servicespring and fall clean uplawn and flowerbed care (pest and weed control)fertilizing plantingand moreCall for a Free estimate!!10% off first months service with signed contract

Please make double sided ( a front and a back)

Target Market(s)

home owners

Industry/Entity Type

Landscape

Requirements
Must have
• please feture the weekly lawn mowing service and then list the other sevices
• contact info... can be found on business card that was uploaded.
• must say residential services
Should not have
• please dont list reo management

```html
<!DOCTYPE html>
<html lang="en">
<head>
<meta charset="utf-8">
<title>Velmora Residential Services – Weekly Lawn Mowing</title>
<link rel="stylesheet" href="https://fonts.googleapis.com/css2?family=Montserrat:ital,wght@0,300;0,500;0,600;1,400&family=Oswald:wght@500&family=Roboto+Condensed:ital,wght@0,400;0,700;1,400&display=swap">
<style>
  :root {
    --grass-light: #3f8f1f;
    --grass-mid: #1f5e12;
    --grass-dark: #062008;
    --cream: #f6e4c4;
    --text-light: #fff8ec;
    --ribbon: #8cc63f;
    --ribbon-dark: #5f9a22;
    --ink: #1b2412;
    --dome: #f4f7f0;
  }
  * { margin: 0; padding: 0; box-sizing: border-box; }
  html, body { width: 848px; height: 1200px; overflow: hidden; background: var(--grass-dark); }
  .postcard {
    position: relative;
    width: 848px;
    height: 1200px;
    overflow: hidden;
    color: var(--text-light);
  }
  .lawn-backdrop {
    position: absolute;
    inset: 0;
    background:
      radial-gradient(ellipse 60% 45% at 62% 22%, var(--grass-light) 0%, rgba(63,143,31,0) 100%),
      radial-gradient(ellipse 80% 70% at 50% 40%, var(--grass-mid) 0%, var(--grass-dark) 100%);
  }
  .brand-dot {
    position: absolute;
    left: 334px;
    top: 200px;
    width: 180px;
    height: 180px;
    border-radius: 50%;
    background: var(--cream);
  }
  .brand-name {
    position: absolute;
    top: 470px;
    left: 0;
    width: 100%;
    text-align: center;
    font-family: "Montserrat", sans-serif;
    font-weight: 500;
    font-size: 108px;
    line-height: 1;
    letter-spacing: -1px;
    color: var(--cream);
  }
  .brand-tagline {
    position: absolute;
    top: 590px;
    left: 0;
    width: 100%;
    text-align: center;
    font-family: "Montserrat", sans-serif;
    font-weight: 300;
    font-size: 21px;
    letter-spacing: 0.62em;
    padding-left: 0.62em;
    color: var(--text-light);
  }
  .headline {
    position: absolute;
    top: 648px;
    left: 0;
    width: 100%;
    text-align: center;
    font-family: "Montserrat", sans-serif;
    font-weight: 500;
    font-size: 33px;
    color: var(--text-light);
  }
  .headline em { font-weight: 400; font-style: italic; }
  .service-list {
    position: absolute;
    top: 703px;
    left: 48px;
    width: 760px;
    display: flex;
    justify-content: space-between;
    list-style: none;
  }
  .service-list li {
    font-family: "Oswald", sans-serif;
    font-weight: 500;
    font-size: 25px;
    line-height: 26px;
    text-align: center;
    text-transform: uppercase;
    letter-spacing: -0.5px;
    padding: 0 14px;
    border-left: 1px solid rgba(255,248,236,0.7);
  }
  .service-list li:first-child { border-left: none; padding-left: 0; }
  .service-list li:last-child { padding-right: 0; }
  .price-badge {
    position: absolute;
    left: 150px;
    top: 800px;
    width: 548px;
    height: 240px;
  }
  .contact {
    position: absolute;
    top: 1074px;
    left: 0;
    width: 100%;
    text-align: center;
    font-family: "Roboto Condensed", sans-serif;
    color: var(--text-light);
  }
  .contact-lead { font-size: 23px; line-height: 32px; }
  .contact-line { font-size: 30px; line-height: 40px; }
  .contact strong { font-weight: 700; }
</style>
</head>
<body>
<main class="postcard">
  <div class="lawn-backdrop" role="img" aria-label="Close-up photograph of a lush green lawn"></div>

  <div class="brand-dot" aria-hidden="true"></div>
  <h1 class="brand-name">VELMORA</h1>
  <p class="brand-tagline">RESIDENTIAL SERVICES</p>

  <h2 class="headline">WEEKLY LAWN MOWING SERVICE <em>and</em></h2>

  <ul class="service-list">
    <li>Fertilizing<br>&amp; Planting</li>
    <li>Pest<br>Control</li>
    <li>Landscape<br>Maintenance</li>
    <li>Snow<br>Removal</li>
    <li>Spring/Fall<br>Clean Up</li>
  </ul>

  <svg class="price-badge" viewBox="0 0 548 240" aria-label="Weekly lawn mowing starting at $15 per cutting">
    <defs>
      <linearGradient id="domeFill" x1="0" y1="0" x2="0" y2="1">
        <stop offset="0" stop-color="#ffffff"/>
        <stop offset="1" stop-color="#dfe8d6"/>
      </linearGradient>
      <path id="ribbonCurve" d="M104,158 Q274,246 444,158"/>
    </defs>
    <path d="M124,172 A150,150 0 0 1 424,172 Z" fill="url(#domeFill)"/>
    <path d="M136,172 A138,138 0 0 1 412,172" fill="none" stroke="var(--ribbon)" stroke-width="4"/>
    <text x="274" y="66" text-anchor="middle" font-family="Roboto Condensed, sans-serif" font-style="italic" font-size="17" fill="var(--ink)">STARTING AT</text>
    <text x="210" y="102" text-anchor="middle" font-family="Roboto Condensed, sans-serif" font-weight="700" font-size="34" fill="var(--ink)">$</text>
    <text x="270" y="144" text-anchor="middle" font-family="Roboto Condensed, sans-serif" font-weight="700" font-size="100" letter-spacing="-4" fill="var(--ink)">15</text>
    <text x="325" y="118" font-family="Roboto Condensed, sans-serif" font-style="italic" font-size="17" fill="var(--ink)">/cutting</text>
    <polygon points="30,152 106,128 118,196 56,214 74,180" fill="var(--ribbon-dark)"/>
    <polygon points="518,152 442,128 430,196 492,214 474,180" fill="var(--ribbon-dark)"/>
    <path d="M96,122 Q274,216 452,122 L436,184 Q274,270 112,184 Z" fill="var(--ribbon)"/>
    <text font-family="Roboto Condensed, sans-serif" font-weight="700" font-size="32" fill="var(--ink)">
      <textPath href="#ribbonCurve" startOffset="50%" text-anchor="middle">WEEKLY LAWN MOWING</textPath>
    </text>
  </svg>

  <footer class="contact">
    <p class="contact-lead">For a <strong>FREE</strong> quote or more information...</p>
    <p class="contact-line">call <strong>(555) 314-2086</strong> or email <strong>VelmoraProperty@email.com</strong></p>
  </footer>
</main>
</body>
</html>
```